Business card for STEADYWAVE

Please design professional business card for IT consulting firm STEADYWAVE INC.
Use logo attached.
Use information from sample qNode business card attached.
replace qnode inc with STEADYWAVE INC.
as well as qnodeinc.com with steadywave.example

```html
<!DOCTYPE html>
<html lang="en">
<head>
<meta charset="utf-8">
<title>STEADYWAVE business card</title>
<link href="https://fonts.googleapis.com/css2?family=Arimo:wght@400;700&family=Montserrat:wght@600&display=swap" rel="stylesheet">
<style>
  :root {
    --bg: #dcdcdc;
    --card: #ffffff;
    --ink: #111111;
    --grey: #6f6f6f;
    --rule: #9a9a9a;
    --orange: #f7941d;
    --purple: #9b1fd6;
    --cyan: #3fd8f5;
    --aqua: #45f5c8;
    --coral: #f26a5a;
  }
  * { margin: 0; padding: 0; box-sizing: border-box; }
  html, body { width: 1200px; height: 802px; overflow: hidden; background: var(--bg); }
  .canvas { position: relative; width: 1200px; height: 802px; }
  .card {
    position: absolute; top: 252px; width: 520px; height: 298px;
    box-shadow: 0 8px 24px rgba(0,0,0,.18);
  }
  .card-front { left: 50px; background: var(--card); }
  .card-back {
    left: 630px;
    background:
      radial-gradient(circle at 0% 100%, var(--orange) 0%, rgba(247,148,29,0) 45%),
      linear-gradient(30deg, var(--coral) 0%, var(--purple) 38%, var(--cyan) 72%, var(--aqua) 100%);
  }
  .brand {
    font-family: "Montserrat", sans-serif; font-weight: 600;
    letter-spacing: .1em; color: var(--ink); white-space: nowrap;
  }
  .front-brand {
    position: absolute; left: 32px; top: 136px; font-size: 21px; line-height: 1;
    display: flex; align-items: center; gap: 8px;
  }
  .brand-square { width: 12px; height: 12px; background: var(--purple); display: inline-block; flex: none; }
  .divider { position: absolute; left: 262px; top: 54px; width: 1px; height: 190px; background: var(--rule); }
  .details { position: absolute; left: 280px; top: 50px; font-family: "Arimo", sans-serif; color: var(--grey); font-size: 11.5px; line-height: 1.42; }
  .person-name { color: var(--orange); font-weight: 700; font-size: 13px; letter-spacing: .02em; }
  .person-title { letter-spacing: .03em; margin-bottom: 10px; }
  .contact-list { list-style: none; margin-bottom: 12px; }
  .contact-list li { display: flex; align-items: center; gap: 7px; }
  .contact-list svg { width: 10px; height: 10px; flex: none; }
  .company-name { color: var(--orange); font-weight: 700; }
  .back-brand { position: absolute; right: 36px; bottom: 44px; font-size: 44px; }
</style>
</head>
<body>
<main class="canvas">
  <section class="card card-front" aria-label="Business card front">
    <div class="brand front-brand">STEADYWAVE<span class="brand-square"></span></div>
    <div class="divider"></div>
    <div class="details">
      <p class="person-name">MAREK DOLANOVSKY, P.ENG.</p>
      <p class="person-title">GENERAL MANAGER</p>
      <ul class="contact-list">
        <li><svg viewBox="0 0 10 10"><path fill="#f7941d" d="M2 0.5 L3.8 2.6 L2.9 3.6 Q4 6 6.4 7.1 L7.4 6.2 L9.5 8 L8.2 9.5 Q3.5 9 0.5 1.8 Z"/></svg>(555) 014-2290 ext.201</li>
        <li><svg viewBox="0 0 10 10"><rect x="2.5" y="0.5" width="5" height="9" rx="1" fill="none" stroke="#f7941d" stroke-width="1.2"/></svg>(555) 017-3846</li>
        <li><svg viewBox="0 0 10 10"><rect x="0.5" y="2" width="9" height="6.5" fill="#f7941d"/><path d="M0.8 2.3 L5 5.8 L9.2 2.3" fill="none" stroke="#fff" stroke-width="1"/></svg>mdolanovsky@steadywave.example</li>
        <li><svg viewBox="0 0 10 10"><circle cx="5" cy="5" r="4.5" fill="#f7941d"/><path d="M0.5 5 H9.5 M5 0.5 Q2 5 5 9.5 M5 0.5 Q8 5 5 9.5" fill="none" stroke="#fff" stroke-width=".8"/></svg>www.steadywave.example</li>
      </ul>
      <p class="company-name">STEADYWAVE INC.</p>
      <p>2180 Harbour Ln., Suite 101</p>
      <p>Oakridge, Ontario, K0A 9Z9, Canada</p>
    </div>
  </section>
  <section class="card card-back" aria-label="Business card back">
    <div class="brand back-brand">STEADYWAVE</div>
  </section>
</main>
</body>
</html>
```